Business Card for IT company

I need a high tech looking business card using our logo. I prefer something clean and modern.

Target Market(s)

Buyers of IT hardware and software, IT Techies who are key influencers

Industry/Entity Type

Business

```html
<!DOCTYPE html>
<html lang="en">
<head>
<meta charset="utf-8">
<title>Kestrel Vale Systems – Business Card</title>
<link href="https://fonts.googleapis.com/css2?family=Bai+Jamjuree:wght@400;500;600&display=swap" rel="stylesheet">
<style>
  :root {
    --backdrop: #6e6e6e;
    --card-dark: #353232;
    --card-light: #f4f4f4;
    --brand-green: #4aaa2c;
    --brand-green-light: #6cc23a;
    --ink: #2f2d2d;
    --paper-text: #f2f2f2;
  }
  * { box-sizing: border-box; margin: 0; padding: 0; }
  html, body {
    width: 1200px; height: 900px; overflow: hidden;
    background: var(--backdrop);
    font-family: "Bai Jamjuree", "Segoe UI", sans-serif;
  }
  .canvas { position: relative; width: 1200px; height: 900px; }

  .card {
    position: absolute;
    left: 267px;
    width: 666px;
    height: 380px;
    overflow: hidden;
    box-shadow: 0 6px 18px rgba(0,0,0,.35);
  }

  /* Back of card */
  .card--back { top: 50px; background: var(--card-dark); }
  .card--back .accent-bar {
    position: absolute;
    right: 0; top: 222px;
    width: 250px; height: 16px;
    background: linear-gradient(90deg, var(--brand-green), var(--brand-green-light));
  }
  .card--back .wordmark {
    position: absolute;
    left: 40px; top: 300px;
    font-size: 40px; font-weight: 500;
    color: var(--paper-text);
    letter-spacing: .5px;
  }

  /* Front of card */
  .card--front { top: 470px; background: var(--card-light); }
  .card--front .wordmark {
    position: absolute;
    left: 150px; top: 34px;
    font-size: 46px; font-weight: 500;
    color: var(--brand-green);
    letter-spacing: .5px;
  }
  .contact-block {
    position: absolute;
    left: 56px; top: 150px;
    padding-left: 16px;
    border-left: 2px solid var(--brand-green-light);
    color: var(--ink);
  }
  .contact-block .person {
    font-size: 24px; font-weight: 400; margin-bottom: 14px;
  }
  .contact-block .person .role {
    font-size: 18px; letter-spacing: .5px;
  }
  .contact-line { font-size: 17px; line-height: 24px; }
  .contact-line .label {
    color: var(--brand-green); font-weight: 600; margin-right: 10px;
  }
  .website {
    position: absolute;
    left: 56px; top: 322px;
    font-size: 17px; color: var(--ink);
  }
  .website .domain { color: var(--brand-green); font-weight: 600; }
</style>
</head>
<body>
<main class="canvas">
  <section class="card card--back" aria-label="Card back">
    <div class="accent-bar"></div>
    <div class="wordmark">Kestrel Vale Systems</div>
  </section>

  <section class="card card--front" aria-label="Card front">
    <div class="wordmark">Kestrel Vale Systems</div>
    <div class="contact-block">
      <p class="person">Mara Lindqvist <span class="role">| MANAGER</span></p>
      <p class="contact-line"><span class="label">t</span>555.014.2290</p>
      <p class="contact-line"><span class="label">e</span>info@kestrelvale.com</p>
      <p class="contact-line">420 Harbor Point Drive, Suite 300, Fairview, VA 20190</p>
    </div>
    <p class="website">www.<span class="domain">kestrelvale</span>.com</p>
  </section>
</main>
</body>
</html>
```